Prairie Hollow - responsive bootstrap website design

Looking to build a responsive service website.

Logo has been provided.

PLEASE REVIEW ATTACHED DESIGN STYLE GUIDES & CLIENT CREATIVE BRIEF FOR OUR REQUIREMENT.

THANK YOU AND GOOD LUCK!

```html
<!DOCTYPE html>
<html lang="en">
<head>
<meta charset="utf-8">
<title>Prairie Hollow Outfitters</title>
<link href="https://fonts.googleapis.com/css2?family=Roboto+Condensed:wght@400;700&family=Roboto:ital,wght@0,400;0,700;1,400&display=swap" rel="stylesheet">
<style>
:root{
  --page:#2a2a2a;
  --header:#2e2e2e;
  --band:#050505;
  --brands:#1b1b1b;
  --footer:#1e1e1e;
  --white:#ffffff;
  --text:#bdbdbd;
  --muted:#8a8a8a;
  --line:#4a4a4a;
  --box:#3a3a3a;
}
*{margin:0;padding:0;box-sizing:border-box}
html,body{width:809px;height:1200px;overflow:hidden}
body{position:relative;background:var(--page);font-family:"Roboto",Arial,sans-serif;color:var(--text)}
.abs{position:absolute}
.site-header{left:0;top:0;width:809px;height:74px;background:var(--header)}
.logo{left:116px;top:14px;width:130px;color:var(--white);font-family:"Roboto Condensed",sans-serif;font-weight:400;font-size:17px;line-height:20px}
.nav{left:0;top:33px;font-size:9px;color:#b8b8b8}
.nav span{position:absolute;white-space:nowrap}
.hero{left:0;top:74px;width:809px;height:364px;background:linear-gradient(180deg,#2f6fb0 0%,#7fb3de 38%,#4f7d52 62%,#1c3446 80%,#0f2333 100%)}
.hero-title{left:118px;top:160px;color:var(--white);font-family:"Roboto Condensed",sans-serif;font-weight:700;text-transform:uppercase;line-height:1}
.hero-title .big{font-size:26px;display:block;margin-bottom:6px}
.hero-title .sub{font-size:16px;display:block;margin-bottom:8px}
.strip{left:126px;top:336px;width:556px;height:92px;background:rgba(0,0,0,.6)}
.thumb{top:344px;width:134px;height:77px}
.strip-arrow{top:374px;color:#9ab;font-size:14px}
.news{left:0;top:438px;width:809px;height:58px;background:var(--band)}
.news-title{left:116px;top:455px;color:var(--white);font-family:"Roboto Condensed",sans-serif;font-weight:700;font-size:14px}
.news-nav{left:192px;top:473px;font-size:8px;color:#999}
.news-rule{left:225px;top:453px;width:1px;height:30px;background:var(--line)}
.news-text{left:242px;top:457px;width:452px;font-size:5.6px;line-height:15px;text-transform:uppercase;color:#c8c8c8}
.section-title{color:var(--white);font-family:"Roboto Condensed",sans-serif;font-weight:700;font-size:14px}
.pager{width:32px;height:15px;display:flex;gap:1px}
.pager span{flex:1;background:#3a3a3a;color:#666;font-size:8px;text-align:center;line-height:15px}
.post-img{top:558px;width:137px;height:119px}
.post-cap{top:685px;font-size:6.5px;color:var(--white);text-transform:uppercase}
.post-date{top:700px;font-size:6.5px;font-style:italic;color:var(--muted)}
.brands{left:0;top:740px;width:809px;height:154px;background:var(--brands)}
.brand{top:799px;width:88px;height:57px;border:2px solid var(--box);display:flex;align-items:center;justify-content:center;color:#6a6a6a;font-family:"Roboto Condensed",sans-serif;font-weight:700;font-size:13px;text-transform:uppercase}
.social-head{top:920px;color:var(--white);font-family:"Roboto Condensed",sans-serif;font-weight:700;font-size:17px}
.avatar{width:32px;height:32px}
.feed{font-size:6.5px;font-style:italic;line-height:13px;color:#9a9a9a}
.more{width:54px;height:17px;background:#1d1d1d;color:#aaa;font-size:5.5px;text-transform:uppercase;text-align:center;line-height:17px}
.site-footer{left:0;top:1138px;width:809px;height:62px;background:var(--footer)}
.foot-links{top:1154px;font-size:7px;color:#bbb}
.foot-links span{position:absolute;white-space:nowrap}
.copy{left:116px;top:1174px;font-size:7px;color:#aaa}
.icon{top:1158px;width:19px;height:19px;border-radius:50%;background:#555}
</style>
</head>
<body>

<header class="abs site-header"></header>
<div class="abs logo">Prairie Hollow<br>&nbsp;&nbsp;&nbsp;&nbsp;Outfitters</div>
<nav class="abs nav">
  <span style="left:290px">Home</span>
  <span style="left:344px">About Us</span>
  <span style="left:410px">Guide Services</span>
  <span style="left:501px">Merchandise</span>
  <span style="left:582px">Video</span>
  <span style="left:635px">Picture Gallery</span>
</nav>

<section class="abs hero" role="img" aria-label="Angler fly casting from rocks beside a river under a blue sky with green hills"></section>
<h1 class="abs hero-title">
  <span class="big">Welcome to</span>
  <span class="sub">Prairie Hollow Outfitters</span>
  <span class="sub">Fishermen in the lowcountry weather</span>
  <span class="sub">Shopping fishing etc</span>
</h1>
<div class="abs strip"></div>
<span class="abs strip-arrow" style="left:116px">&#8249;</span>
<span class="abs strip-arrow" style="left:687px">&#8250;</span>
<div class="abs thumb" style="left:134px;background:linear-gradient(#5d9fd8,#3b6c52)" role="img" aria-label="Angler casting by the river"></div>
<div class="abs thumb" style="left:270px;background:linear-gradient(#9fc3e0,#6b5a48)" role="img" aria-label="Angler holding a caught fish"></div>
<div class="abs thumb" style="left:405px;background:linear-gradient(#3d6fa8,#2a3440)" role="img" aria-label="Two divers with a large fish"></div>
<div class="abs thumb" style="left:540px;background:linear-gradient(#7a9a7a,#8a8478)" role="img" aria-label="Group on a dock with a hanging catch"></div>

<section class="abs news"></section>
<h2 class="abs news-title">LATEST NEWS</h2>
<span class="abs news-nav">&#8249; &#8250;</span>
<div class="abs news-rule"></div>
<p class="abs news-text">It is a long established fact that a reader will be distracted by the readable content of a page when looking at its layout. The point of using lorem ipsum is that it has a more-or-less normal distribution of letters, as opposed...</p>

<h2 class="abs section-title" style="left:116px;top:526px">RECENT POSTS</h2>
<div class="abs pager" style="left:661px;top:527px"><span>&#8249;</span><span>&#8250;</span></div>
<div class="abs post-img" style="left:116px;background:linear-gradient(#4d8ea8,#6fb0c0)" role="img" aria-label="School of fish underwater"></div>
<div class="abs post-img" style="left:263px;background:linear-gradient(#6fa4d6,#1d4f86)" role="img" aria-label="Angler fishing at sea"></div>
<div class="abs post-img" style="left:410px;background:linear-gradient(#1e5fb8,#0f3e88)" role="img" aria-label="Marlin leaping from blue water"></div>
<div class="abs post-img" style="left:557px;background:linear-gradient(135deg,#7a8a6a,#c0b0a0)" role="img" aria-label="Colourful fishing lures in a tackle box"></div>
<p class="abs post-cap" style="left:116px">Fishermen in the lowcountry</p>
<p class="abs post-cap" style="left:263px">Fishermen in the lowcountry</p>
<p class="abs post-cap" style="left:410px">Fishermen in the lowcountry</p>
<p class="abs post-cap" style="left:557px">Fishermen in the lowcountry</p>
<p class="abs post-date" style="left:116px">Posted on 27 march 2014</p>
<p class="abs post-date" style="left:263px">Posted on 27 march 2014</p>
<p class="abs post-date" style="left:410px">Posted on 27 march 2014</p>
<p class="abs post-date" style="left:557px">Posted on 27 march 2014</p>

<section class="abs brands"></section>
<h2 class="abs section-title" style="left:116px;top:767px">OUR BRANDS</h2>
<div class="abs pager" style="left:661px;top:767px"><span>&#8249;</span><span>&#8250;</span></div>
<div class="abs brand" style="left:116px">Alder</div>
<div class="abs brand" style="left:214px">Brookline</div>
<div class="abs brand" style="left:312px">Tidewell</div>
<div class="abs brand" style="left:410px">Korvan</div>
<div class="abs brand" style="left:507px">Redfin</div>
<div class="abs brand" style="left:605px">Marlow Reels</div>

<h2 class="abs social-head" style="left:116px">Friendwall</h2>
<h2 class="abs social-head" style="left:312px">Chirpline</h2>
<h2 class="abs social-head" style="left:514px">Snapframe</h2>

<div class="abs avatar" style="left:116px;top:953px;background:#b08a70" role="img" aria-label="Member portrait"></div>
<div class="abs avatar" style="left:116px;top:1000px;background:#c8b080" role="img" aria-label="Member portrait"></div>
<div class="abs avatar" style="left:116px;top:1048px;background:#a08870" role="img" aria-label="Member portrait"></div>
<div class="abs avatar" style="left:312px;top:953px;background:#c0a888" role="img" aria-label="Member portrait"></div>
<div class="abs avatar" style="left:312px;top:1000px;background:#a07860" role="img" aria-label="Member portrait"></div>
<div class="abs avatar" style="left:312px;top:1048px;background:#b89878" role="img" aria-label="Member portrait"></div>
<div class="abs avatar" style="left:514px;top:953px;background:#9a7a68" role="img" aria-label="Member portrait"></div>
<div class="abs avatar" style="left:514px;top:1000px;background:#b89080" role="img" aria-label="Member portrait"></div>
<div class="abs avatar" style="left:514px;top:1048px;background:#a88a78" role="img" aria-label="Member portrait"></div>

<p class="abs feed" style="left:156px;top:953px">Many desktop publishing packages<br>and web page editors now use...</p>
<p class="abs feed" style="left:156px;top:1000px">Many desktop publishing packages<br>and web page editors now use...</p>
<p class="abs feed" style="left:156px;top:1048px">Many desktop publishing packages<br>and web page editors now use...</p>
<p class="abs feed" style="left:352px;top:953px">Many desktop publishing packages<br>and web page editors now use...</p>
<p class="abs feed" style="left:352px;top:1000px">Many desktop publishing packages<br>and web page editors now use...</p>
<p class="abs feed" style="left:352px;top:1048px">Many desktop publishing packages<br>and web page editors now use...</p>
<p class="abs feed" style="left:554px;top:953px">Many desktop publishing packages<br>and web page editors now use...</p>
<p class="abs feed" style="left:554px;top:1000px">Many desktop publishing packages<br>and web page editors now use...</p>
<p class="abs feed" style="left:554px;top:1048px">Many desktop publishing packages<br>and web page editors now use...</p>

<div class="abs more" style="left:116px;top:1091px">View more</div>
<div class="abs more" style="left:312px;top:1091px">View more</div>
<div class="abs more" style="left:514px;top:1091px">View more</div>

<footer class="abs site-footer"></footer>
<nav class="abs foot-links" style="left:0">
  <span style="left:116px">Home</span>
  <span style="left:155px">About Us</span>
  <span style="left:205px">Guide Services</span>
  <span style="left:273px">Merchandise</span>
  <span style="left:334px">Video</span>
  <span style="left:373px">Picture Gallery</span>
</nav>
<p class="abs copy">Copyright &copy; 2014 Prairie Hollow Outfitters. All rights reserved.</p>
<div class="abs icon" style="left:572px"></div>
<div class="abs icon" style="left:597px"></div>
<div class="abs icon" style="left:622px"></div>
<div class="abs icon" style="left:647px"></div>
<div class="abs icon" style="left:673px"></div>

</body>
</html>
```